Letterhead

Can you please design me a letterhead that I can use electronically in word as a template. I have attached my business card as I would like the design to reflect this logo.

```html
<!DOCTYPE html>
<html lang="en">
<head>
<meta charset="utf-8">
<title>Tessera Letterhead</title>
<link href="https://fonts.googleapis.com/css2?family=Open+Sans:wght@400;600;700&display=swap" rel="stylesheet">
<style>
  :root {
    --backdrop: #e4e4e4;
    --paper: #ffffff;
    --brand-red: #b3121b;
    --ink: #1c1c1c;
    --ink-soft: #444444;
    --watermark: #f1f1f1;
    --band-black: #0d0d0d;
  }
  * { margin: 0; padding: 0; box-sizing: border-box; }
  html, body {
    width: 1200px;
    height: 900px;
    overflow: hidden;
    background: var(--backdrop);
    font-family: "Open Sans", Arial, sans-serif;
  }
  .letterhead {
    position: absolute;
    left: 296px;
    top: 20px;
    width: 608px;
    height: 860px;
    background: var(--paper);
    overflow: hidden;
    box-shadow: 0 2px 10px rgba(0,0,0,0.12);
  }
  .brand {
    position: absolute;
    left: 200px;
    top: 50px;
    display: flex;
    align-items: center;
    gap: 10px;
  }
  .brand-mark {
    width: 14px;
    height: 14px;
    background: var(--brand-red);
  }
  .brand-name {
    font-weight: 600;
    font-size: 28px;
    line-height: 1;
    color: var(--ink);
  }
  .brand-watermark {
    position: absolute;
    right: -4px;
    top: 24px;
    writing-mode: vertical-rl;
    font-weight: 400;
    font-size: 100px;
    line-height: 1;
    color: var(--watermark);
    user-select: none;
  }
  .sender {
    position: absolute;
    right: 22px;
    top: 758px;
    font-size: 10px;
    line-height: 1.55;
    color: var(--ink-soft);
  }
  .sender-name { font-weight: 700; font-size: 11px; color: var(--ink); }
  .sep { color: var(--brand-red); margin: 0 3px; }
  .role { color: var(--brand-red); font-weight: 600; }
  .label { color: var(--brand-red); }
  .footer-band {
    position: absolute;
    left: 0;
    bottom: 24px;
    width: 100%;
    height: 22px;
    display: flex;
  }
  .footer-band .band-red { flex: 0 0 77%; background: var(--brand-red); }
  .footer-band .band-black { flex: 1; background: var(--band-black); }
</style>
</head>
<body>
  <main class="letterhead">
    <header class="brand">
      <span class="brand-mark" aria-hidden="true"></span>
      <span class="brand-name">tessera</span>
    </header>

    <div class="brand-watermark" aria-hidden="true">tessera</div>

    <footer class="sender">
      <div><span class="sender-name">Margaret Ellison</span><span class="sep">|</span><span class="role">Principal</span></div>
      <div><span class="label">P:</span> 0400 518 374<span class="sep">|</span><span class="label">E:</span> margaret@tessera.net.au<span class="sep">|</span><span class="label">ACN:</span> 012 345 678</div>
    </footer>

    <div class="footer-band" aria-hidden="true">
      <div class="band-red"></div>
      <div class="band-black"></div>
    </div>
  </main>
</body>
</html>
```